General Contractors need a new Crisp updated Card Design

We need a new business card design for our company of 25 years based in Toronto call Pollvarn Building Inc. : Our goal is to be the leading commercial contractors in Toronto by providing exceptional value to our clients. We work very hard to deliver professional, quality, service in conjunction with consistent price competitiveness to all of our clients on every single project.

Target Market(s)

Design & Build Clients

Industry/Entity Type

Construction Company

Contact Information for Business Card

Address:
18 West Marlow Field Road, Unit 17, Dunmore Vale, ON, K7T 2M9
Office: 905-218-6937

Pollvarns Logo
Employee Job Description
Employee Cell Phone #
Employee Email
www.pollvarn.example

Colors

Designer to choose colors to be used in the design.

Requirements
Must have
• Quote Company Saying:
• "Professional. Quality. Service."
Nice to have
• New Crisp up to date look. simple & fresh ( Not to Busy)
Should not have
• NO BLUE PRINTS ON THE BUSINESS CARDS

```html
<!DOCTYPE html>
<html lang="en">
<head>
<meta charset="utf-8">
<title>Pollvarn Building Inc. – Business Card</title>
<link rel="stylesheet" href="https://fonts.googleapis.com/css2?family=Arimo:wght@400;700&display=swap">
<style>
  :root {
    --stage: #1f2023;
    --teal: #0b7467;
    --teal-deep: #08685c;
    --teal-soft: #1a8375;
    --white: #ffffff;
    --grey-text: #6b6f70;
    --grey-rule: #9a9d9e;
  }
  * { box-sizing: border-box; margin: 0; padding: 0; }
  html, body { width: 1200px; height: 800px; overflow: hidden; }
  body {
    background: var(--stage);
    font-family: "Arimo", Arial, sans-serif;
    position: relative;
  }
  .card {
    position: absolute;
    width: 560px;
    height: 320px;
    box-shadow: 0 14px 30px rgba(0,0,0,.45);
    overflow: hidden;
  }
  /* Front side */
  .card--front {
    left: 80px; top: 70px;
    background: var(--teal);
    color: var(--white);
  }
  .front__map {
    position: absolute;
    left: 50px; top: 40px;
    width: 460px; height: 230px;
    border-radius: 50%;
    background: radial-gradient(ellipse at center, var(--teal-soft) 0%, rgba(26,131,117,.45) 55%, rgba(11,116,103,0) 75%);
  }
  .front__brand {
    position: absolute;
    left: 0; right: 0; top: 112px;
    display: flex; align-items: center; justify-content: center;
    gap: 16px;
  }
  .brand__mark {
    width: 46px; height: 46px;
    border: 2px solid currentColor;
  }
  .brand__name {
    font-weight: 700;
    font-size: 34px;
    letter-spacing: .5px;
    line-height: 1;
  }
  .front__tagline {
    position: absolute;
    left: 0; right: 0; top: 204px;
    text-align: center;
    font-size: 13px;
    letter-spacing: 4px;
  }
  /* Back side */
  .card--back {
    left: 560px; top: 410px;
    background: var(--white);
    color: var(--teal);
  }
  .back__brand {
    position: absolute;
    left: 34px; top: 96px;
    display: flex; align-items: center; gap: 12px;
  }
  .back__brand .brand__mark { width: 38px; height: 38px; background: var(--teal); border: none; }
  .back__brand .brand__name { font-size: 26px; }
  .back__contacts {
    position: absolute;
    right: 26px; top: 26px;
    list-style: none;
    text-align: right;
    font-size: 12px;
    color: var(--grey-text);
    line-height: 20px;
  }
  .back__contacts li { display: flex; justify-content: flex-end; align-items: center; gap: 8px; }
  .back__contacts svg { width: 12px; height: 12px; fill: var(--teal); }
  .back__person {
    position: absolute;
    left: 34px; top: 196px;
  }
  .person__name { font-weight: 700; font-size: 17px; letter-spacing: .4px; }
  .person__role { font-size: 13px; color: var(--grey-text); margin-top: 2px; }
  .person__cell { font-size: 12px; color: var(--grey-text); margin-top: 6px; display: flex; align-items: center; gap: 7px; }
  .person__cell svg { width: 11px; height: 11px; stroke: var(--teal); fill: none; stroke-width: 2; }
  .back__rule {
    position: absolute; left: 0; right: 0; bottom: 34px;
    height: 4px; background: var(--grey-rule);
  }
  .back__band {
    position: absolute; left: 0; right: 0; bottom: 0;
    height: 34px; background: var(--teal-deep);
    color: var(--white);
    font-size: 12.5px;
    display: flex; align-items: center; justify-content: center;
    letter-spacing: .2px;
  }
</style>
</head>
<body>

<section class="card card--front">
  <div class="front__map" role="img" aria-label="Faint world map decoration in soft teal"></div>
  <div class="front__brand">
    <span class="brand__mark"></span>
    <span class="brand__name">Pollvarn Building Inc.</span>
  </div>
  <p class="front__tagline">PROFESSIONAL. QUALITY. SERVICE</p>
</section>

<section class="card card--back">
  <ul class="back__contacts">
    <li>905-218-6937
      <svg viewBox="0 0 24 24" aria-hidden="true"><path d="M6.6 10.8a15 15 0 0 0 6.6 6.6l2.2-2.2c.3-.3.7-.4 1-.2 1.1.4 2.3.6 3.6.6.6 0 1 .4 1 1V20c0 .6-.4 1-1 1A17 17 0 0 1 3 4c0-.6.4-1 1-1h3.5c.6 0 1 .4 1 1 0 1.3.2 2.5.6 3.6.1.3 0 .7-.2 1z"/></svg>
    </li>
    <li>info@pollvarn.example
      <svg viewBox="0 0 24 24" aria-hidden="true"><path d="M2 5h20v14H2z M2 5l10 8 10-8" /></svg>
    </li>
    <li>www.pollvarn.example
      <svg viewBox="0 0 24 24" aria-hidden="true"><circle cx="12" cy="12" r="10"/></svg>
    </li>
  </ul>

  <div class="back__brand">
    <span class="brand__mark"></span>
    <span class="brand__name">Pollvarn Building Inc.</span>
  </div>

  <div class="back__person">
    <p class="person__name">DANIEL FERROW</p>
    <p class="person__role">Director</p>
    <p class="person__cell">
      <svg viewBox="0 0 12 12" aria-hidden="true"><rect x="1" y="1" width="10" height="10"/></svg>
      416-730-2285
    </p>
  </div>

  <div class="back__rule"></div>
  <div class="back__band">18 West Marlow Field Road, Unit 17, Dunmore Vale, ON, K7T 2M9</div>
</section>

</body>
</html>
```